Business Card Design

I need a Business Card that will catch the attention that will not get thrown in a Drawer. I have 23 companies I use for Auto, Home, Life, and Business Insurance. I make sure that people have the best coverage for the $ spent.

Industry/Entity Type

Business

Contact Information for Business Card

Dorlin Insurance Agency, Inc., Marcus Helgren, 4375 West Tamber Lane Larkfield, Westmere 45192 555-281-7496, www.dorlinagency.example, Friendnet, Workline, Circleup

```html
<!DOCTYPE html>
<html lang="en">
<head>
<meta charset="utf-8">
<title>Dorlin Insurance Agency – Business Card</title>
<link href="https://fonts.googleapis.com/css2?family=Sorts+Mill+Goudy&display=swap" rel="stylesheet">
<style>
  :root {
    --orange: #f47920;
    --orange-fade: rgba(244, 121, 32, 0);
    --brown: #4a2e17;
    --white: #ffffff;
    --photo-blue: #2f63b8;
    --photo-skin: #d9a27f;
    --shadow: rgba(0, 0, 0, 0.28);
  }
  * { margin: 0; padding: 0; box-sizing: border-box; }
  html, body {
    width: 1200px; height: 702px; overflow: hidden;
    background: var(--white);
  }
  .card {
    position: relative; width: 1200px; height: 702px;
    background: var(--white);
    font-family: "Sorts Mill Goudy", "Goudy Old Style", Georgia, serif;
  }
  .rule-top {
    position: absolute; left: 0; top: 91px; width: 1200px; height: 13px;
    background: linear-gradient(to right, var(--orange-fade) 0%, var(--orange) 6%, var(--orange) 92%, var(--orange-fade) 100%);
  }
  .agency-frame {
    position: absolute; left: 218px; top: 41px; width: 785px; height: 110px;
    border: 11px solid var(--orange); border-radius: 18px;
    background: var(--white);
    display: flex; align-items: center; justify-content: center;
  }
  .agency-name {
    font-size: 52px; color: var(--brown); font-weight: 400;
    text-shadow: 3px 3px 4px var(--shadow);
    white-space: nowrap;
  }
  .contact-panel {
    position: absolute; left: 381px; top: 204px; width: 819px; height: 307px;
    border-radius: 9px 0 0 9px;
    background: linear-gradient(to right, var(--orange) 0%, var(--orange) 62%, var(--orange-fade) 100%);
    color: var(--white);
    padding: 16px 0 0 5px;
    font-size: 36px; line-height: 55px;
  }
  .contact-panel p { white-space: nowrap; }
  .contact-panel .call-label { margin-top: 2px; }
  .portrait {
    position: absolute; left: 31px; top: 243px; width: 298px; height: 395px;
    background: linear-gradient(to bottom, var(--white) 0%, var(--photo-skin) 25%, var(--photo-skin) 58%, var(--photo-blue) 70%, var(--photo-blue) 100%);
  }
  .person-name {
    position: absolute; left: 351px; top: 554px;
    font-size: 55px; color: var(--brown);
    text-shadow: 3px 3px 4px var(--shadow);
    white-space: nowrap;
  }
  .social-links {
    position: absolute; right: 16px; top: 566px;
    display: flex; gap: 18px;
    font-size: 22px; color: var(--brown);
  }
  .social-links span { white-space: nowrap; }
  .rule-bottom {
    position: absolute; left: 0; top: 624px; width: 1200px; height: 14px;
    background: linear-gradient(to right, var(--orange) 0%, var(--orange) 84%, var(--orange-fade) 100%);
  }
</style>
</head>
<body>
  <div class="card">
    <div class="rule-top"></div>
    <div class="agency-frame">
      <h1 class="agency-name">Dorlin Insurance Agency, Inc.</h1>
    </div>

    <div class="contact-panel">
      <p>4375 West Tamber Lane Larkfield</p>
      <p>www.dorlinagency.example</p>
      <p>Westmere 45192</p>
      <p class="call-label">Call Today:</p>
      <p>555.281.7496</p>
    </div>

    <div class="rule-bottom"></div>
    <div class="portrait" role="img" aria-label="Portrait photo of agent Marcus Helgren in a blue shirt"></div>
    <div class="person-name">Marcus Helgren</div>

    <div class="social-links">
      <span>Friendnet</span>
      <span>Circleup</span>
      <span>Workline</span>
    </div>
  </div>
</body>
</html>
```